Email Signature Gif Animation Design

We are looking for an interactive Email Signature to Standardize around for our growing company.

We are a commerical electrical contractor based out of North Jersey. We have a big corporate client tele and perfer a more professional fresh looking signature with titles and perhaps a suttle animation for effect.

Attached below is our company logo which is to be used prominently in the emai signature. We would consider a "refresh' of our logo design provided it does deviate too much.

We would like the tag Line "The KALV Electric Way" worked into that signature as a option.
Updates

Reviewing designs and am underwhelmed with the creativiity and designs, this is anyones prize!

Target Market(s)

Corporate / Middle Managers

Industry/Entity Type

Electrical Contracting & Engineering

Colors
FFF300
FFF600
FEFA6F
FFFEC7
FFFEE8

Requirements
Must have
• Must have, First & Last Name of Employee, Title of Employee, Office & Cell Phone Number, Email Address
Nice to have
• Gif Animation

```html
<!DOCTYPE html>
<html lang="en">
<head>
<meta charset="utf-8">
<title>KALV Electric – Email Signature</title>
<link rel="stylesheet" href="https://fonts.googleapis.com/css2?family=Fira+Sans:wght@400;800&family=Jost:wght@400;500&family=Caveat:wght@700&display=swap">
<style>
  :root {
    --stage: #525252;
    --card: #ffffff;
    --ink: #1b1b1b;
    --gold: #d9b521;
    --caption: #f2f2f2;
    --photo-top: #e9e6e2;
    --photo-bottom: #4a72c9;
  }
  * { box-sizing: border-box; margin: 0; padding: 0; }
  html, body { width: 1200px; height: 828px; overflow: hidden; }
  body { background: var(--stage); position: relative; font-family: "Jost", sans-serif; }

  .signature {
    position: absolute; left: 230px; top: 96px; width: 739px; height: 539px;
    background: var(--card);
  }
  .divider {
    position: absolute; left: 312px; top: 42px; width: 3px; height: 455px;
    background: var(--ink);
  }

  /* Left column */
  .portrait { position: absolute; left: 54px; top: 56px; width: 204px; height: 234px; }
  .social { position: absolute; left: 57px; top: 322px; display: flex; gap: 17px; list-style: none; }
  .social li {
    width: 35px; height: 35px; border-radius: 50%;
    background: var(--ink); border: 3px solid var(--gold);
  }
  .brand-mark {
    position: absolute; left: 0; width: 312px; top: 386px; text-align: center;
    font-family: "Fira Sans", sans-serif; font-weight: 800; font-size: 36px;
    color: var(--ink); letter-spacing: 0.5px; line-height: 1;
  }
  .tagline {
    position: absolute; left: 0; width: 312px; top: 462px; text-align: center;
    font-family: "Caveat", cursive; font-weight: 700; font-size: 28px; color: var(--ink);
  }

  /* Right column */
  .name {
    position: absolute; left: 350px; top: 74px;
    font-family: "Fira Sans", sans-serif; font-weight: 800; font-size: 38px;
    color: var(--ink); letter-spacing: 0.5px; line-height: 1;
  }
  .title {
    position: absolute; left: 350px; top: 121px; width: 335px; height: 29px;
    background: var(--ink); color: var(--card); text-align: center;
    font-family: "Fira Sans", sans-serif; font-weight: 400; font-size: 25px; line-height: 29px;
  }
  .contacts { position: absolute; left: 350px; top: 197px; list-style: none; }
  .contacts li { display: flex; align-items: center; height: 35px; margin-bottom: 10px; }
  .contacts .icon {
    width: 35px; height: 35px; border-radius: 50%; background: var(--ink);
    display: flex; align-items: center; justify-content: center; flex: none;
  }
  .contacts span {
    margin-left: 14px; font-size: 20px; font-weight: 500; color: var(--ink);
  }
  .company {
    position: absolute; left: 350px; top: 405px; display: flex; align-items: center; gap: 10px;
  }
  .company .square { width: 22px; height: 22px; background: var(--gold); }
  .company span {
    font-family: "Fira Sans", sans-serif; font-weight: 800; font-size: 24px;
    color: var(--ink); letter-spacing: 1px;
  }

  .caption {
    position: absolute; left: 0; width: 1200px; top: 702px; text-align: center;
    font-family: "Jost", sans-serif; font-size: 32px; color: var(--caption); letter-spacing: 0.5px;
  }
</style>
</head>
<body>
  <section class="signature">
    <svg class="portrait" viewBox="0 0 204 234" role="img" aria-label="Employee portrait photo in a gold hexagon frame">
      <defs>
        <linearGradient id="photoFill" x1="0" y1="0" x2="0" y2="1">
          <stop offset="0" stop-color="var(--photo-top)"/>
          <stop offset="0.55" stop-color="#d8c2b2"/>
          <stop offset="1" stop-color="var(--photo-bottom)"/>
        </linearGradient>
      </defs>
      <polygon points="102,4 200,60 200,174 102,230 4,174 4,60" fill="url(#photoFill)" stroke="var(--gold)" stroke-width="6"/>
    </svg>

    <ul class="social" aria-label="Social profiles">
      <li aria-label="Social profile 1"></li>
      <li aria-label="Social profile 2"></li>
      <li aria-label="Social profile 3"></li>
      <li aria-label="Social profile 4"></li>
    </ul>

    <div class="brand-mark">KALV Electric</div>
    <p class="tagline">“The KALV Electric Way”</p>

    <div class="divider"></div>

    <h1 class="name">MARLON VASQUEZ</h1>
    <p class="title">Support Team Leader</p>

    <ul class="contacts">
      <li>
        <div class="icon">
          <svg width="20" height="18" viewBox="0 0 20 18"><path d="M1 6c0-3 4-4 9-4s9 1 9 4v1h-4V5H5v2H1z" fill="#fff"/><rect x="3" y="8" width="14" height="9" rx="2" fill="#fff"/><circle cx="10" cy="12.5" r="2.6" fill="var(--ink)"/></svg>
        </div>
        <span>+1 5550148273</span>
      </li>
      <li>
        <div class="icon">
          <svg width="12" height="20" viewBox="0 0 12 20"><rect x="1" y="1" width="10" height="18" rx="2" fill="none" stroke="#fff" stroke-width="2"/><rect x="3" y="4" width="6" height="10" fill="#fff"/><circle cx="6" cy="16.5" r="1" fill="#fff"/></svg>
        </div>
        <span>+1 5550148273</span>
      </li>
      <li>
        <div class="icon">
          <svg width="20" height="14" viewBox="0 0 20 14"><rect x="1" y="1" width="18" height="12" rx="1.5" fill="none" stroke="#fff" stroke-width="2"/><path d="M1 1l9 7 9-7M1 13l7-6M19 13l-7-6" fill="none" stroke="#fff" stroke-width="1.6"/></svg>
        </div>
        <span>marlon@kalvelectric.com</span>
      </li>
      <li>
        <div class="icon">
          <svg width="20" height="20" viewBox="0 0 20 20" fill="none" stroke="#fff" stroke-width="1.5"><circle cx="10" cy="10" r="8.5"/><ellipse cx="10" cy="10" rx="4" ry="8.5"/><path d="M1.5 10h17M10 1.5v17M3 5.5h14M3 14.5h14"/></svg>
        </div>
        <span>www.kalvelectric.com</span>
      </li>
    </ul>

    <div class="company">
      <div class="square"></div>
      <span>KALV ELECTRIC LLC</span>
    </div>
  </section>

  <p class="caption">animated gif will be created once you like the design</p>
</body>
</html>
```